Website Header Development

I am after a redesign of the Header of a website www.kaltroweb.com.au.
This project is for the header only, and should fit in with the rest of the site
Target Market(s)
Business
Requirements
Should not have
- Over the top. Keep it simple

```html
<!DOCTYPE html>
<html lang="en">
<head>
<meta charset="utf-8">
<title>Kaltro Energy – Resource Efficiency</title>
<link href="https://fonts.googleapis.com/css2?family=Alegreya:wght@700;800&family=Alegreya+Sans:wght@400;500;700;800&family=Open+Sans:wght@400&display=swap" rel="stylesheet">
<style>
  :root {
    --navy: #1a2e8a;
    --heading-navy: #0c1a7a;
    --sidebar-blue: #26449a;
    --green: #1f7f3d;
    --green-dark: #1a6e34;
    --text: #111111;
    --muted: #6f6f6f;
    --sky: #bfe4f4;
    --white: #ffffff;
    --field-border: #c9c9c9;
  }
  * { box-sizing: border-box; margin: 0; padding: 0; }
  html, body { width: 1200px; height: 911px; overflow: hidden; background: var(--white); }
  body { position: relative; font-family: "Alegreya Sans", sans-serif; color: var(--text); }

  .site-header {
    position: absolute; left: 0; top: 0; width: 1200px; height: 140px;
    background: linear-gradient(100deg, #ffffff 0%, #f4fafd 30%, #e3f2f9 55%, #d2ecf7 75%, #eaf6fb 100%);
    border-top: 2px solid #c7d8e6;
  }
  .brand {
    position: absolute; left: 36px; top: 52px;
    display: flex; align-items: center; gap: 14px;
    font-family: "Alegreya Sans", sans-serif; font-weight: 700;
    font-size: 44px; letter-spacing: -0.5px; color: var(--navy);
  }
  .brand-mark { width: 30px; height: 30px; background: var(--navy); border-radius: 50%; }
  .header-visual {
    position: absolute; right: 0; top: 0; width: 290px; height: 140px;
    background: radial-gradient(circle at 60% 45%, #3a8fd0 0%, #7cc1e6 30%, #cfe9f5 60%, rgba(255,255,255,0) 80%);
  }

  .main-nav {
    position: absolute; left: 0; top: 140px; width: 1200px; height: 62px;
    background: linear-gradient(90deg, var(--green) 0%, var(--green) 70%, var(--green-dark) 100%);
  }
  .main-nav a {
    position: absolute; color: var(--white); text-decoration: none;
    font-family: "Alegreya Sans", sans-serif; font-size: 15px; font-weight: 500; top: 15px;
  }
  .main-nav a.is-featured { font-size: 18px; font-weight: 700; top: 19px; }

  .page-title {
    position: absolute; left: 60px; top: 240px; width: 720px; text-align: center;
    font-family: "Alegreya", serif; font-weight: 800; font-size: 29px; color: var(--heading-navy);
  }
  .intro-questions {
    position: absolute; left: 71px; top: 300px; width: 240px;
    font-size: 17px; line-height: 30px;
  }
  .intro-questions p { margin-bottom: 31px; }
  .intro-visual {
    position: absolute; left: 344px; top: 313px; width: 419px; height: 279px;
    background: linear-gradient(90deg, #e4e6e9 0%, #cfd3d8 55%, #e8e9eb 100%);
  }
  .body-copy { position: absolute; left: 71px; width: 700px; font-size: 17px; line-height: 30px; }
  .body-copy.is-muted { color: var(--muted); }

  .sidebar { position: absolute; left: 881px; top: 204px; width: 240px; }
  .search-field {
    width: 220px; height: 36px; border: 1px solid var(--field-border); border-radius: 3px;
    display: flex; align-items: center; gap: 8px; padding-left: 10px;
    font-family: "Open Sans", sans-serif; font-size: 16px; color: #9a9a9a;
  }
  .newsletter-title {
    margin-top: 48px; width: 180px;
    font-family: "Alegreya", serif; font-weight: 800; font-size: 25px; line-height: 36px;
    letter-spacing: 2px; color: var(--sidebar-blue);
  }
  .newsletter-copy { font-size: 13px; font-weight: 800; line-height: 30px; width: 230px; }
  .newsletter-field { width: 210px; height: 34px; border: 1px solid var(--field-border); margin: 14px 0 18px; }
</style>
</head>
<body>
  <header class="site-header">
    <div class="brand"><span>kaltro energy</span><span class="brand-mark"></span></div>
    <div class="header-visual" role="img" aria-label="Light bulb containing a globe and green field"></div>
  </header>

  <nav class="main-nav">
    <a class="is-featured" style="left:99px">Home</a>
    <a style="left:189px">About Us</a>
    <a style="left:284px">Services</a>
    <a style="left:370px">Projects and Case Studies</a>
    <a class="is-featured" style="left:564px">Financial Information</a>
    <a style="left:776px">News</a>
    <a style="left:847px">Contact</a>
  </nav>

  <h1 class="page-title">Resource Efficiency – Sustainable Solutions</h1>

  <div class="intro-questions">
    <p>Is your business performing as well as your competitors?</p>
    <p>Are your fixed costs comparable to industry leaders?</p>
    <p>Is your business becoming less profitable with increased energy, waste and water prices?</p>
  </div>
  <div class="intro-visual" role="img" aria-label="Businessman holding puzzle pieces labelled Solution"></div>

  <p class="body-copy" style="top:631px">Do you wish to reduce your impact on the environment through reducing the use of resources (energy, waste and water) within your business?</p>
  <p class="body-copy is-muted" style="top:722px">If so, Kaltro can assist your business to achieve its core functions in the most effective manner.</p>
  <p class="body-copy is-muted" style="top:813px">Kaltro can assist your business in achieving improved productivity through the implementation of:</p>

  <aside class="sidebar">
    <div class="search-field">
      <svg width="16" height="16" viewBox="0 0 16 16"><circle cx="6.5" cy="6.5" r="4.5" fill="none" stroke="#9a9a9a" stroke-width="2"/><line x1="10" y1="10" x2="14.5" y2="14.5" stroke="#9a9a9a" stroke-width="2.4"/></svg>
      <span>Search</span>
    </div>
    <h2 class="newsletter-title">Kaltro Energy Newsletter</h2>
    <p class="newsletter-copy" style="margin-top:20px">Would you like to receive our regular monthly Newsletter? Please fill in your Name:</p>
    <div class="newsletter-field"></div>
    <p class="newsletter-copy">Let us know your email address so we can send the Newsletter directly to your email address. (Note that your details will not be passed onto any 3rd parties. Your details stricly remain with Kaltro Energy for the purposes of sending you the Kaltro Energy Newsletter)</p>
    <div class="newsletter-field"></div>
    <p class="newsletter-copy">Further, please let us know if there are particular topics you would like to</p>
  </aside>
</body>
</html>
```